Business Cards and Stationery for Brook Harlow Supply & Advisory sàrl
Simple
Karim Ait Lounes
Associé gérant
CP 7148
CH-1002 Lausanne
Switzerland
kal@brookharlow.ch
www.brookharlow.ch
Business cards to look fresh, in alignment with logo branding.
Colour scheme, images and writting to coordinate with logo.
We may soon need to change our office address and, possibly add phone and fax numbers, so we need to use a font that I can modify.
We want to use the logo designed through Tessavane.

```html
<!DOCTYPE html>
<html lang="fr">
<head>
<meta charset="utf-8">
<title>Brook Harlow Supply &amp; Advisory – Stationery</title>
<link href="https://fonts.googleapis.com/css2?family=Open+Sans:wght@400;700&display=swap" rel="stylesheet">
<style>
  :root{
    --bg-deep:#f2a200;
    --bg-light:#ffd21c;
    --green:#3f9a2e;
    --green-light:#8cc63f;
    --paper:#ffffff;
    --ink:#4a4a4a;
    --muted:#888888;
    --line:#c9c9c9;
    --card-grey:#5d5d5d;
    --envelope:#f7f7f7;
    --watermark:rgba(140,198,63,.13);
  }
  *{box-sizing:border-box;margin:0;padding:0}
  html,body{width:1200px;height:322px;overflow:hidden}
  body{font-family:"Open Sans",Arial,sans-serif;color:var(--ink)}
  .presentation{
    position:relative;width:1200px;height:322px;
    background:radial-gradient(ellipse at 50% 45%,var(--bg-light) 0%,var(--bg-deep) 85%);
    border:5px solid var(--paper);
  }
  .item{position:absolute;background:var(--paper);box-shadow:1px 2px 4px rgba(0,0,0,.25);overflow:hidden}
  .brand{display:flex;align-items:center;gap:5px;font-weight:700;color:var(--green);white-space:nowrap}
  .brand .dot{border-radius:50%;background:var(--green-light);flex:none}
  .brand--sm{font-size:9px}.brand--sm .dot{width:10px;height:10px}
  .brand--md{font-size:12px}.brand--md .dot{width:13px;height:13px}
  .tiny{font-size:5px;line-height:7px}
  .footer-band{position:absolute;left:0;right:0;bottom:5px;height:3px;background:var(--green)}
  .footer-text{position:absolute;left:0;right:0;bottom:10px;text-align:center;font-size:5px;line-height:6px;color:var(--green)}
  .watermark{position:absolute;border-radius:50%;background:var(--watermark)}

  /* business cards */
  .card-front{left:38px;top:38px;width:200px;height:106px}
  .card-front .contact{position:absolute;right:10px;top:9px;text-align:right;font-size:6px;line-height:8px;color:var(--muted)}
  .card-front .name{font-weight:700;font-size:7px;line-height:9px;color:var(--green)}
  .card-front .brand{position:absolute;left:12px;top:64px}
  .card-back{left:38px;top:156px;width:200px;height:106px;background:var(--card-grey);display:flex;align-items:center;justify-content:center}
  .card-back .brand{color:var(--paper)}

  /* invoice */
  .invoice{left:252px;top:34px;width:146px;height:250px;padding:12px 10px}
  .invoice .brand{justify-content:center;margin-bottom:12px}
  .invoice .fields{display:grid;grid-template-columns:1fr 1fr;gap:4px 8px;margin-bottom:10px;color:var(--muted)}
  .invoice .field{border-bottom:.5px solid var(--line)}
  .invoice table{width:100%;border-collapse:collapse;font-size:5px;line-height:7px}
  .invoice th{background:var(--green);color:var(--paper);font-weight:700;padding:1px 2px;text-align:left}
  .invoice td{border:.5px solid var(--line);height:9px}

  /* letterheads */
  .letter{top:34px;width:146px;height:250px;padding:12px 10px}
  .letter-a{left:440px}
  .letter-b{left:630px}
  .letter .brand{justify-content:center}
  .letter .addr{position:absolute;right:10px;top:34px;text-align:right;color:var(--muted)}
  .letter .body-lines{position:absolute;left:12px;right:12px;top:84px}
  .letter .body-lines span{display:block;height:1px;background:#e3e3e3;margin-bottom:6px}
  .letter-b .brand{position:absolute;left:0;right:0;top:118px}

  /* envelopes */
  .envelope-back{left:802px;top:96px;width:170px;height:104px;background:var(--envelope)}
  .envelope-back svg{position:absolute;inset:0;width:100%;height:100%}
  .envelope-front{left:792px;top:170px;width:180px;height:104px;padding:10px}
  .envelope-front .window{position:absolute;right:14px;bottom:22px;width:70px;height:26px;border:.5px solid var(--line)}

  /* shirts */
  .shirt{position:absolute;background:var(--paper);border-radius:6px 6px 2px 2px;box-shadow:1px 2px 4px rgba(0,0,0,.25);display:flex;justify-content:center}
  .shirt-small{left:984px;top:114px;width:84px;height:150px;padding-top:32px}
  .shirt-large{left:1078px;top:92px;width:106px;height:184px;padding-top:46px}
  .shirt-large .mark{width:58px;height:58px;border-radius:50%;background:var(--green-light)}
</style>
</head>
<body>
<main class="presentation">

  <section class="item card-front" aria-label="Business card front">
    <div class="contact">
      <p class="name">Karim Ait Lounes</p>
      <p>Associé gérant</p>
      <p>CP 7148 · CH-1002 Lausanne</p>
      <p>Switzerland</p>
      <p>kal@brookharlow.ch</p>
    </div>
    <div class="brand brand--md"><span class="dot"></span>Brook Harlow</div>
    <div class="footer-band"></div>
  </section>

  <section class="item card-back" aria-label="Business card back">
    <div class="brand brand--md"><span class="dot"></span>Brook Harlow</div>
  </section>

  <section class="item invoice" aria-label="Invoice">
    <div class="brand brand--sm"><span class="dot"></span>Brook Harlow</div>
    <div class="fields tiny">
      <p class="field">Facture</p><p class="field">Date</p>
      <p class="field">Client</p><p class="field">N°</p>
    </div>
    <table>
      <thead><tr><th>Description</th><th>Qté</th><th>Prix</th><th>Total</th></tr></thead>
      <tbody>
        <tr><td></td><td></td><td></td><td></td></tr><tr><td></td><td></td><td></td><td></td></tr>
        <tr><td></td><td></td><td></td><td></td></tr><tr><td></td><td></td><td></td><td></td></tr>
        <tr><td></td><td></td><td></td><td></td></tr><tr><td></td><td></td><td></td><td></td></tr>
        <tr><td></td><td></td><td></td><td></td></tr><tr><td></td><td></td><td></td><td></td></tr>
        <tr><td></td><td></td><td></td><td></td></tr><tr><td></td><td></td><td></td><td></td></tr>
      </tbody>
    </table>
    <div class="footer-band"></div>
    <p class="footer-text">www.brookharlow.ch</p>
  </section>

  <section class="item letter letter-a" aria-label="Letterhead">
    <div class="brand brand--sm"><span class="dot"></span>Brook Harlow</div>
    <div class="addr tiny"><p>CP 7148</p><p>CH-1002 Lausanne</p><p>Objet</p></div>
    <div class="watermark" style="left:38px;top:120px;width:70px;height:70px"></div>
    <div class="body-lines"><span></span><span></span><span></span><span></span><span></span></div>
    <div class="footer-band"></div>
    <p class="footer-text">www.brookharlow.ch</p>
  </section>

  <section class="item letter letter-b" aria-label="Compliments slip">
    <div class="watermark" style="left:38px;top:90px;width:70px;height:70px"></div>
    <div class="brand brand--md"><span class="dot"></span>Brook Harlow</div>
    <div class="footer-band"></div>
    <p class="footer-text">www.brookharlow.ch</p>
  </section>

  <section class="item envelope-back" aria-label="Envelope back">
    <svg viewBox="0 0 170 104" preserveAspectRatio="none">
      <path d="M0 0 L85 52 L170 0" fill="none" stroke="#d8d8d8" stroke-width="1"/>
    </svg>
  </section>

  <section class="item envelope-front" aria-label="Envelope front">
    <div class="brand brand--sm"><span class="dot"></span>Brook Harlow</div>
    <div class="window"></div>
    <div class="footer-band"></div>
  </section>

  <div class="shirt shirt-small" role="img" aria-label="White T-shirt with the company name on the chest">
    <div class="brand brand--sm"><span class="dot"></span>Brook Harlow</div>
  </div>
  <div class="shirt shirt-large" role="img" aria-label="White T-shirt back with a large green circle">
    <div class="mark"></div>
  </div>

</main>
</body>
</html>
```